Velto Works CBD Packaging Label Design. Creative Modern Minimalist. Future Work possible!!!

Creating a CBD product.Bottle size is height 84mm diameter 25mmLabel size 74mm x 38mmMatch Stick Box: 40mm x 100mm x 50mm
Pippette cap is red FYI.
NOTE: We have added a logo file but I am also paying for a new logo design. So do as you please.Need the packaging and labelling done for CBD product. Name is Velto Works. Logo is included in file below. I have also added some product packaging and design for inspiration. No need to use this but to give you an idea. Some flexibility with label dimensions. In so far as, it must fit on the base of the bottle, think eye dropper.

The last brimloft cbd oil dropper is a cool industrial design but we would prefer a design with a label.Red and white are the main colors. Minimalist, modern, clean, swiss cross in the mix are acceptable.

Also, the logo image with the textured background on the business card is part of then look we would like to package. Not a requirement but certainly a consideration.Feel free to reach out for any further questions.Below are some specs and text we need to squeeze on then packaging / labelling.

The location of the text or emphasis is NOT fixed even if it specifies the location in the description below.

Box must contain:
logo, velto Works text
Warnings-(warning sign with exclamation mark) not suitable for consumption -under 18 restricted sign?
PACKAGING TEXT (Classic rectangular)
LogoCanna Labs (below logo)10% CBD Oil (x milligram mg)10ml
Disclaimers (From dorvexi)
MEDICAL: (From dorvexi website) Disclaimer: Velto Works products are sold without any medical claims; they have not been proven to treat, relieve, nor cure any disease or medical condition. please refer to the terms and conditions (need to read these from)
CONTACT: Avoid contact during pregnancy and while nursing. Do not get in eyes, on skin, or on clothing. Get medical advice/attention if you feel unwell.ADVICE: Keep out of reach of children. Protect from sunlight. Store in a well-ventilated place. Keep cool. Refrigerate after opening.
Ingredients: Ingredients: 80% MCT oil, 20% Carmagnola Selezionata (What terpenes?check with clear horizon). 100% organic. (Check labeling) Extracted using ethanol extraction.

Side note: More information about boxing size and bottle can be seen on a competitiors site. shown below.

https://dorvexi.example/product-category/selection/

Target Market(s)

CBD oil users in Europe

Logo Text

velto works

Font styles to use
Serif
Sans Serif
Script

Requirements
Must have
• I want textured, like business card texture considered for the label. The box is a standard cardboard for the moment. Pharma grade product. I would like it to stand out in a pharmacy but not look out of place.
• We need all sides of the packaging. Use lorem ipsum if you have to. Some of the text is above though
Should not have
• Nothing that references the weed leaf. Keep that off

```html
<!DOCTYPE html>
<html lang="en">
<head>
<meta charset="utf-8">
<title>Velto Works CBD Oil Packaging</title>
<link rel="stylesheet" href="https://fonts.googleapis.com/css2?family=Oswald:wght@300;400;500;700&family=Roboto:wght@400;500&family=Fjalla+One&display=swap">
<style>
  :root {
    --red: #e3101f;
    --red-deep: #8e0e16;
    --black: #111111;
    --white: #ffffff;
    --panel-grey: #ededed;
    --beige: #d7c8b0;
    --ink: #2b2b2b;
    --side-ink: #555555;
    --stage: #e6e6e6;
  }
  * { margin: 0; padding: 0; box-sizing: border-box; }
  html, body { width: 1200px; height: 935px; overflow: hidden; }
  body {
    background: var(--stage);
    font-family: "Roboto", Arial, sans-serif;
    position: relative;
  }

  /* ---------- box: side panel ---------- */
  .box-side {
    position: absolute; left: 150px; top: 190px;
    width: 210px; height: 560px;
    background: linear-gradient(90deg, #f4f4f4, var(--panel-grey));
    overflow: hidden;
  }
  .side-copy { padding: 58px 14px 0 10px; font-family: "Fjalla One", "Oswald", sans-serif; color: var(--side-ink); }
  .side-title { color: var(--red); font-size: 13px; font-weight: 400; margin-bottom: 12px; }
  .side-list { list-style: none; font-size: 8.5px; line-height: 11px; margin-bottom: 22px; }
  .side-list li::before { content: "• "; }
  .side-list.conditions li { padding-left: 6px; text-indent: -6px; }
  .side-sub { color: var(--red); font-size: 8.5px; margin-bottom: 10px; }
  .side-ingredients { font-size: 8px; line-height: 10.5px; }
  .side-band {
    position: absolute; left: 0; bottom: 0; width: 100%; height: 82px;
    background: linear-gradient(135deg, var(--red), var(--red-deep) 60%, var(--black));
  }

  /* ---------- box: front panel ---------- */
  .box-front {
    position: absolute; left: 360px; top: 190px;
    width: 270px; height: 560px;
    background: var(--white);
    overflow: hidden;
  }
  .brand { display: flex; align-items: center; justify-content: center; gap: 8px; }
  .brand-dot { width: 12px; height: 12px; border-radius: 50%; background: var(--red); }
  .brand-name { font-family: "Roboto", sans-serif; font-weight: 400; color: var(--red); font-size: 15px; }
  .box-front .brand { margin-top: 70px; }
  .strength { font-family: Arial, "Roboto", sans-serif; color: var(--ink); font-size: 11px; line-height: 13px; margin: 26px 0 0 46px; }
  .swiss-flag { display: block; }
  .box-front .swiss-flag { margin: 18px auto 0; }
  .front-band {
    position: absolute; left: 0; top: 192px; width: 100%; height: 136px;
    background: linear-gradient(135deg, #c8101c, var(--red-deep) 45%, var(--black) 75%, var(--red));
  }
  .product-name { position: absolute; font-family: "Oswald", sans-serif; font-weight: 400; color: var(--beige); line-height: .88; }
  .box-front .product-name { left: 10px; top: 340px; }
  .product-name .cbd { font-size: 100px; display: block; letter-spacing: -2px; }
  .product-name .oil { font-size: 58px; display: block; }
  .seal { position: absolute; }
  .box-front .seal { right: 14px; top: 440px; }
  .volume { font-family: "Fjalla One", "Oswald", sans-serif; color: var(--red); font-size: 22px; position: absolute; left: 0; width: 100%; text-align: center; }
  .box-front .volume { bottom: 28px; }

  /* ---------- bottle label ---------- */
  .label {
    position: absolute; left: 720px; top: 260px;
    width: 330px; height: 400px;
    background: var(--white);
    overflow: hidden;
  }
  .label .brand { margin-top: 64px; }
  .label .strength { margin: 26px 0 0 28px; }
  .label .swiss-flag { position: absolute; right: 50px; top: 160px; }
  .label .product-name { left: 16px; top: 186px; }
  .label .product-name .cbd { font-size: 96px; }
  .label .product-name .oil { font-size: 52px; }
  .label .seal { right: 32px; top: 240px; }
  .label-band {
    position: absolute; left: 0; bottom: 0; width: 100%; height: 66px;
    background: linear-gradient(90deg, var(--red-deep), #c8101c 35%, var(--red));
  }
  .label .volume { color: var(--white); bottom: 16px; font-size: 24px; }
</style>
</head>
<body>

  <section class="box-side" aria-label="Box side panel">
    <div class="side-copy">
      <h2 class="side-title">Medical Benefits of “CBD”</h2>
      <ul class="side-list">
        <li>Pain relief</li><li>Anti-anxiety</li><li>Anti-psychotic</li><li>Muscle relaxant</li>
        <li>Anti-cancer</li><li>Anti-seizure</li><li>Anti-inflammatory</li><li>Neuroprotective</li>
      </ul>
      <p class="side-sub">CBD shows promise in the treatment of several conditions:</p>
      <ul class="side-list conditions">
        <li>Cronic Pain</li>
        <li>Hepatitis C, especially active disease</li>
        <li>Reduces inflammation and fibrosis</li>
        <li>Psychiatric illness (anxiety, bipolar, schizophrenia)</li>
        <li>Seizure disorders and other central nervous conditions</li>
        <li>Insomnia</li>
        <li>Inflammatory disorders such as rheumatoid arthritis</li>
        <li>Patients who enjoy the benefits of cannabis but don't want psychoactive effects or have an anxiety, panic response to cannabis</li>
      </ul>
      <p class="side-sub">INGREDIENTS:</p>
      <p class="side-ingredients">80% MCT oil, 20% Cannabis sativa flower extract oil (monoterpenes, sesquiterpenes, terpenophenolics). 100% organic. Semi-Decarboxylated flower extract oil (monoterpenes, sesquiterpenes, terpenophenolics). 100% organic. Semi-Decarboxylated</p>
    </div>
    <div class="side-band" role="img" aria-label="Red and black decorative graphic band"></div>
  </section>

  <section class="box-front" aria-label="Box front panel">
    <div class="brand"><span class="brand-dot"></span><span class="brand-name">Velto Works</span></div>
    <p class="strength">10% CBD OIL<br>(X MILLIGRAM MG)10ML</p>
    <svg class="swiss-flag" width="30" height="30" viewBox="0 0 32 32" aria-label="Swiss cross">
      <rect width="32" height="32" fill="var(--red)"/>
      <rect x="13" y="6" width="6" height="20" fill="#fff"/><rect x="6" y="13" width="20" height="6" fill="#fff"/>
    </svg>
    <div class="front-band" role="img" aria-label="Red and black decorative graphic band"></div>
    <h1 class="product-name"><span class="cbd">CBD</span><span class="oil">OIL</span></h1>
    <svg class="seal" width="60" height="60" viewBox="0 0 66 66" aria-label="Quality seal">
      <circle cx="33" cy="33" r="30" fill="none" stroke="var(--red)" stroke-width="2"/>
      <circle cx="33" cy="33" r="22" fill="none" stroke="#333" stroke-width="1"/>
    </svg>
    <p class="volume">50 ml</p>
  </section>

  <section class="label" aria-label="Bottle label">
    <div class="brand"><span class="brand-dot"></span><span class="brand-name">Velto Works</span></div>
    <p class="strength">10% CBD OIL<br>(X MILLIGRAM MG)10ML</p>
    <svg class="swiss-flag" width="30" height="30" viewBox="0 0 32 32" aria-label="Swiss cross">
      <rect width="32" height="32" fill="var(--red)"/>
      <rect x="13" y="6" width="6" height="20" fill="#fff"/><rect x="6" y="13" width="20" height="6" fill="#fff"/>
    </svg>
    <h2 class="product-name"><span class="cbd">CBD</span><span class="oil">OIL</span></h2>
    <svg class="seal" width="60" height="60" viewBox="0 0 66 66" aria-label="Quality seal">
      <circle cx="33" cy="33" r="30" fill="none" stroke="var(--red)" stroke-width="2"/>
      <circle cx="33" cy="33" r="22" fill="none" stroke="#333" stroke-width="1"/>
    </svg>
    <div class="label-band"></div>
    <p class="volume">50 ml</p>
  </section>

</body>
</html>
```